Business Card Design for Cybersecurity Company - Quorvent Systems

We need a business card design for our new cybersecurity company, Quorvent. We’re going for a clean, hi tech look that feels modern, premium, and trustworthy. We want a design that really stands out and makes people say WOW when we hand it over!

Quorvent delivers reliable IT support and managed services for small and mid sized businesses. We help companies stay secure, efficient, and connected through proactive monitoring, cybersecurity services, cloud management, and remote support.

Target Market(s)

Designers should target small and mid sized businesses that need dependable cybersecurity and IT support.

Industry/Entity Type

Cybersecurity, Managed Service Provider, IT services

Contact Information for Business Card

Contact information

Requirements
Must have
• The card should look clean, modern, and tech focused, with the Quorvent logo, clear contact info, and strong readability. It needs to feel premium and professional while still keeping a simple layout that fits a cybersecurity and IT brand.
Nice to have
• Nice to have elements include subtle touches that give the card a modern, tech feel, along with a layout that works well in different background styles.
Should not have
• The card should avoid clutter, loud graphics, or anything that takes attention away from the logo and contact details.

```html
<!DOCTYPE html>
<html lang="en">
<head>
<meta charset="utf-8">
<title>Quorvent Systems — Business Card</title>
<link href="https://fonts.googleapis.com/css2?family=Sora:wght@600&family=Inter:wght@400&display=swap" rel="stylesheet">
<style>
  :root {
    --backdrop: #bfbfbf;
    --card: #252525;
    --ink: #ffffff;
    --muted: #b4b4b4;
  }
  * { margin: 0; padding: 0; box-sizing: border-box; }
  html, body { width: 1200px; height: 802px; overflow: hidden; background: var(--backdrop); }
  .sheet {
    width: 1200px; height: 802px;
    display: flex; align-items: center; justify-content: center; gap: 24px;
  }
  .card {
    position: relative;
    width: 540px; height: 310px;
    background: var(--card);
    border-radius: 14px;
    box-shadow: 0 6px 18px rgba(0,0,0,.18);
    color: var(--ink);
    font-family: "Inter", Arial, sans-serif;
  }
  .holder-name {
    position: absolute; left: 22px; top: 16px;
    font-family: "Sora", Arial, sans-serif; font-weight: 600;
    font-size: 24px; letter-spacing: -0.5px;
  }
  .holder-role {
    position: absolute; right: 22px; top: 26px;
    font-size: 13px; color: var(--muted);
  }
  .brand {
    position: absolute; left: 50%; top: 50%;
    transform: translate(-50%, -50%);
    display: flex; align-items: center; gap: 12px;
    font-family: "Sora", Arial, sans-serif; font-weight: 600;
    font-size: 26px; color: var(--ink); white-space: nowrap;
  }
  .brand-mark {
    width: 34px; height: 34px; border-radius: 50%;
    border: 3px solid var(--ink);
  }
  .contact {
    position: absolute; bottom: 18px;
    font-size: 13px; display: flex; gap: 14px;
  }
  .contact-phones { left: 22px; }
  .contact-online { right: 20px; flex-direction: column; gap: 8px; align-items: flex-end; }
  .contact-item { display: flex; align-items: center; gap: 6px; }
  .contact-online .contact-item { flex-direction: row; }
  .icon { width: 13px; height: 13px; fill: none; stroke: var(--ink); stroke-width: 2; }
</style>
</head>
<body>
<main class="sheet">
  <section class="card card-front" aria-label="Card front">
    <h1 class="holder-name">Dorian Keller</h1>
    <p class="holder-role">Owner | CEO | Quorvent Systems</p>
    <div class="brand"><span class="brand-mark"></span>Quorvent Systems</div>
    <div class="contact contact-phones">
      <span class="contact-item">
        <svg class="icon" viewBox="0 0 16 16"><rect x="2" y="6" width="12" height="8" rx="2"/><path d="M1 6c2-4 12-4 14 0"/></svg>
        (555) 014 2290
      </span>
      <span class="contact-item">
        <svg class="icon" viewBox="0 0 16 16"><path d="M3 2l3 1 1 3-2 1c1 2 2 3 4 4l1-2 3 1 1 3c-6 1-12-5-11-11z"/></svg>
        (555) 238-7716
      </span>
    </div>
    <div class="contact contact-online">
      <span class="contact-item">dorian@quorvent.com
        <svg class="icon" viewBox="0 0 16 16"><path d="M1 8l14-6-5 13-2-6z"/></svg>
      </span>
      <span class="contact-item">www.quorvent.com
        <svg class="icon" viewBox="0 0 16 16"><circle cx="8" cy="8" r="6.5"/><path d="M1.5 8h13M8 1.5c3 3 3 10 0 13M8 1.5c-3 3-3 10 0 13"/></svg>
      </span>
    </div>
  </section>
  <section class="card card-back" aria-label="Card back">
    <div class="brand"><span class="brand-mark"></span>Quorvent Systems</div>
  </section>
</main>
</body>
</html>
```